beauty salon application for consumer

- Find your favorite beauty salons and spas or discover new places next to you with geolocation;
- Filter your search by price, distance, category and type of service;
- Never worry again about having to schedule during your work hours or about not having your calls answered when you want to book an appointment;
- Mark salons as favorites and be the first to be informed of exclusive discounts;
- Don’t ever forget your appointments with Glow Nook’s notifications;
- Compare prices, places and services freely, in a quick and practical way;
- Share reviews about services and places you go with other users and read their opinions;
- USER-FRIENDLY INTERFACE
- GALLERY
- OFFERS

similar interface with application name "primlane"

Industry/Entity Type

Beauty Salon

Font styles to use
Decorative
Script

Colors

Designer to choose colors to be used in the design.

Requirements
Must have
• Please have a look into these applications:
• 1- https://apps.example-store.test/gb/app/primlane/id502918377/?pid=corvella&c=footer-link
• 2- https://apps.example-store.test/us/app/fizz-ltd-book-curl-set-glam-nail-services/id6093817245
• 3- https://market.sample-apps.test/store/apps/details?id=com.lumiparlour.user&hl=en
• 4- https://apps.example-store.test/app/id361720498?mt=8
Nice to have
• Nice to give me a clear screenshots for main function of the application ,please see the above applications before giving me a design .

```html
<!DOCTYPE html>
<html lang="en">
<head>
<meta charset="utf-8">
<title>primlane – Search and Discover</title>
<link rel="stylesheet" href="https://fonts.googleapis.com/css2?family=Roboto:wght@400;500;700&display=swap">
<style>
  :root {
    --canvas-bg: #ededed;
    --teal: #0a7b9e;
    --teal-deep: #07566e;
    --teal-light: #15a6a2;
    --card-bg: #ffffff;
    --ink: #1a1a1a;
    --ink-soft: #333333;
    --star-on: #f39a12;
    --star-off: #b9b9b9;
    --divider: #dcdcdc;
    --heading-blue: #0f6f95;
    --photo-warm: #b28a55;
    --photo-dark: #3f3a33;
  }
  * { box-sizing: border-box; margin: 0; padding: 0; }
  html, body { width: 1200px; height: 1200px; overflow: hidden; }
  body {
    background: var(--canvas-bg);
    font-family: "Roboto", sans-serif;
    position: relative;
  }

  .section-tag {
    position: absolute;
    left: 700px; top: 48px;
    width: 452px; height: 88px;
    border: 3px solid var(--heading-blue);
    border-radius: 44px;
    display: flex; align-items: center; justify-content: center;
    color: var(--heading-blue);
    font-weight: 700;
    font-size: 36px;
    letter-spacing: 2px;
  }

  .app-screen {
    position: absolute;
    left: 100px; top: 100px;
    width: 563px; height: 1000px;
    background: linear-gradient(180deg, var(--teal) 0%, var(--teal) 55%, var(--teal-light) 100%);
    overflow: hidden;
    color: #fff;
    box-shadow: 0 10px 40px rgba(0,0,0,.12);
  }

  .status-bar {
    height: 30px;
    display: flex; align-items: center; justify-content: space-between;
    padding: 0 10px;
    font-size: 17px; font-weight: 500;
  }
  .status-bar .carrier, .status-bar .battery { display: flex; align-items: center; gap: 5px; }

  .toolbar {
    display: flex; justify-content: space-between; align-items: center;
    padding: 20px 20px 0 20px;
    height: 60px;
  }

  .screen-title {
    margin: 42px 0 0 22px;
    font-size: 39px; font-weight: 500;
  }

  .search-field {
    position: absolute;
    left: 22px; top: 201px;
    width: 518px; height: 76px;
    background: var(--teal-deep);
    border-radius: 38px;
    display: flex; align-items: center; justify-content: space-between;
    padding: 0 8px 0 35px;
    font-size: 25px;
  }
  .search-field .search-button {
    width: 60px; height: 60px; border-radius: 50%;
    background: #fff;
    display: flex; align-items: center; justify-content: center;
  }

  .section-label {
    position: absolute;
    left: 22px; top: 344px;
    font-size: 24px; font-weight: 500;
  }

  .side-card {
    position: absolute;
    top: 425px; height: 520px; width: 70px;
    background: var(--card-bg);
    border-radius: 8px;
    overflow: hidden;
  }
  .side-card.left { left: -40px; }
  .side-card.right { right: -40px; }
  .side-card .side-photo { height: 270px; background: linear-gradient(135deg, #d9d3cf, #a89890); }

  .salon-card {
    position: absolute;
    left: 56px; top: 398px;
    width: 450px; height: 572px;
    background: var(--card-bg);
    border-radius: 8px;
    overflow: hidden;
    color: var(--ink);
    box-shadow: 0 6px 20px rgba(0,0,0,.18);
  }
  .salon-photo {
    height: 299px;
    background: linear-gradient(180deg, var(--photo-warm) 0%, #c9a470 45%, var(--photo-dark) 100%);
  }
  .salon-name {
    text-align: center; margin-top: 18px;
    font-size: 26px; font-weight: 700;
  }
  .salon-area {
    text-align: center; margin-top: 4px;
    font-size: 24px; color: var(--ink-soft);
  }
  .rating {
    display: flex; justify-content: center; gap: 8px; margin-top: 10px;
  }
  .card-divider {
    height: 2px; background: var(--divider);
    margin: 14px 22px 0 22px;
  }
  .services {
    display: flex; align-items: center; gap: 12px;
    margin: 20px 22px 0 22px;
    font-size: 22px; color: var(--ink-soft);
    white-space: nowrap; overflow: hidden;
  }
  .book-button {
    position: absolute;
    left: 15px; right: 15px; bottom: 15px;
    height: 60px; border-radius: 30px;
    background: linear-gradient(90deg, #11a39b, var(--teal));
    color: #fff;
    display: flex; align-items: center; justify-content: space-between;
    padding: 0 40px 0 44px;
    font-size: 24px; font-weight: 500; letter-spacing: 1px;
  }
</style>
</head>
<body>

  <div class="section-tag">SEARCH &amp; DISCOVER</div>

  <main class="app-screen">
    <div class="status-bar">
      <span class="carrier">
        <svg width="22" height="14" viewBox="0 0 22 14" fill="#fff"><rect x="0" y="9" width="3" height="5"/><rect x="5" y="6" width="3" height="8"/><rect x="10" y="3" width="3" height="11"/><rect x="15" y="0" width="3" height="14"/></svg>
        Nova
        <svg width="18" height="14" viewBox="0 0 18 14" fill="none" stroke="#fff" stroke-width="2"><path d="M1 5a12 12 0 0 1 16 0M4 8a7 7 0 0 1 10 0"/><circle cx="9" cy="12" r="1.5" fill="#fff" stroke="none"/></svg>
      </span>
      <span class="clock">9:41 AM</span>
      <span class="battery">
        <svg width="10" height="16" viewBox="0 0 10 16" fill="none" stroke="#fff" stroke-width="1.5"><path d="M1 4l8 8-4 3V1l4 3-8 8"/></svg>
        100%
        <svg width="36" height="16" viewBox="0 0 36 16"><rect x="1" y="1" width="30" height="14" rx="3" fill="none" stroke="#fff" stroke-width="1.5"/><rect x="3" y="3" width="26" height="10" rx="1.5" fill="#fff"/><rect x="32" y="5" width="3" height="6" rx="1" fill="#fff"/></svg>
      </span>
    </div>

    <div class="toolbar">
      <svg class="close-icon" width="24" height="24" viewBox="0 0 24 24" stroke="#fff" stroke-width="3" stroke-linecap="round"><path d="M3 3l18 18M21 3L3 21"/></svg>
      <svg class="filter-icon" width="34" height="32" viewBox="0 0 34 32" fill="#fff"><path d="M0 0h34L21 15v13l-8 4V15z"/></svg>
    </div>

    <h1 class="screen-title">Search and Discover</h1>

    <div class="search-field">
      <span class="placeholder">Search beauty salon</span>
      <span class="search-button">
        <svg width="32" height="32" viewBox="0 0 32 32" fill="none" stroke="var(--teal-deep)" stroke-width="3.5" stroke-linecap="round"><circle cx="13" cy="13" r="9"/><path d="M20 20l9 9"/></svg>
      </span>
    </div>

    <h2 class="section-label">Featured Salons in Vancouver</h2>

    <div class="side-card left"><div class="side-photo" role="img" aria-label="Photo of a salon interior with nail polish shelves"></div></div>
    <div class="side-card right"><div class="side-photo" role="img" aria-label="Photo of a salon reception area"></div></div>

    <article class="salon-card">
      <div class="salon-photo" role="img" aria-label="Photo of the salon storefront and reception desk"></div>
      <h3 class="salon-name">Solace Salon and Spa</h3>
      <p class="salon-area">Harbour Court</p>
      <div class="rating" aria-label="Rated 3 out of 5">
        <svg width="30" height="30" viewBox="0 0 30 30"><circle cx="15" cy="15" r="13" fill="none" stroke="var(--star-on)" stroke-width="2"/><path d="M15 7l2.4 5.2 5.6.6-4.2 3.8 1.2 5.6L15 19.4l-5 2.8 1.2-5.6L7 12.8l5.6-.6z" fill="var(--star-on)"/></svg>
        <svg width="30" height="30" viewBox="0 0 30 30"><circle cx="15" cy="15" r="13" fill="none" stroke="var(--star-on)" stroke-width="2"/><path d="M15 7l2.4 5.2 5.6.6-4.2 3.8 1.2 5.6L15 19.4l-5 2.8 1.2-5.6L7 12.8l5.6-.6z" fill="var(--star-on)"/></svg>
        <svg width="30" height="30" viewBox="0 0 30 30"><circle cx="15" cy="15" r="13" fill="none" stroke="var(--star-on)" stroke-width="2"/><path d="M15 7l2.4 5.2 5.6.6-4.2 3.8 1.2 5.6L15 19.4l-5 2.8 1.2-5.6L7 12.8l5.6-.6z" fill="var(--star-on)"/></svg>
        <svg width="30" height="30" viewBox="0 0 30 30"><circle cx="15" cy="15" r="13" fill="none" stroke="var(--star-off)" stroke-width="2"/><path d="M15 7l2.4 5.2 5.6.6-4.2 3.8 1.2 5.6L15 19.4l-5 2.8 1.2-5.6L7 12.8l5.6-.6z" fill="var(--star-off)"/></svg>
        <svg width="30" height="30" viewBox="0 0 30 30"><circle cx="15" cy="15" r="13" fill="none" stroke="var(--star-off)" stroke-width="2"/><path d="M15 7l2.4 5.2 5.6.6-4.2 3.8 1.2 5.6L15 19.4l-5 2.8 1.2-5.6L7 12.8l5.6-.6z" fill="var(--star-off)"/></svg>
      </div>
      <div class="card-divider"></div>
      <p class="services">
        <svg width="24" height="22" viewBox="0 0 24 22" fill="#444"><rect x="1" y="0" width="22" height="6" rx="2"/><rect x="2" y="8" width="20" height="13" rx="2"/><rect x="5" y="11" width="14" height="3" fill="#fff"/></svg>
        Manicure, Pedicure, Facial, Mas...
      </p>
      <div class="book-button">
        <span>BOOK NOW</span>
        <svg width="30" height="30" viewBox="0 0 30 30" fill="none" stroke="#fff" stroke-width="2.5"><rect x="3" y="5" width="24" height="22" rx="2"/><path d="M3 11h24M9 2v6M21 2v6"/><g fill="#fff" stroke="none"><rect x="7" y="14" width="4" height="3"/><rect x="13" y="14" width="4" height="3"/><rect x="19" y="14" width="4" height="3"/><rect x="7" y="20" width="4" height="3"/><rect x="13" y="20" width="4" height="3"/><rect x="19" y="20" width="4" height="3"/></g></svg>
      </div>
    </article>
  </main>

</body>
</html>
```